Redesign

Hello,

I want you to redesign this page: www.pravilo.com

I like the colors and would like to keep it 'airy', I don't want it to be the same boring website, although it needs to be easily navigational and user friendly.

NOTE: The websites main objective is to get people to signup to get our RSS services, the main task of the site is NOT a property search page, it is just a sub.

I am excited to see your designs.

Pages I am looking to have designed:
http://www.pravilo.com/
http://shortlinkory.com/q8vn27k
http://www.pravilo.com/advertise-your-real-estate.php
http://www.pravilo.com/submit-your-real-estate-listings.php
http://www.pravilo.com/2800/
http://www.pravilo.com/members/-/43

I HAVE POSTED A LARGER LOGO FOR YOU TO WORK WITH, I WANT THE LOGO TO BE INCORPORATED IN THE HEADER, NOT JUST STUCK THERE.

Owen
Updates

Hello,

I have made the project committed and I will chose one of your designs.

The current designs are nice but I really want the header to have the logo built into it, not have the logo just stuck in a box.

I also like the homepage designs with tiled sold homes, that is a great visual for the potential clients.

Thank you for your submissions so far.

Owen

Industry/Entity Type

Real Estate

```html
<!DOCTYPE html>
<html lang="en">
<head>
<meta charset="utf-8">
<title>Pravilo — Online Real Estate Marketing Simplified</title>
<link rel="stylesheet" href="https://fonts.googleapis.com/css2?family=Nunito+Sans:wght@400;600;700&family=Noto+Serif:wght@400;700&display=swap">
<style>
:root{
  --blue:#2b86c5;
  --blue-dark:#1f6fa8;
  --blue-text:#2a8ac6;
  --orange:#f6a623;
  --green:#5cb82e;
  --gray-bg:#f1f1f1;
  --footer:#4a4a4a;
  --text:#444;
  --white:#fff;
}
*{box-sizing:border-box;margin:0;padding:0}
html,body{width:800px;height:1200px;overflow:hidden}
body{font-family:"Nunito Sans",Arial,sans-serif;color:var(--text);background:var(--white);position:relative}
.wrap{position:absolute;left:86px;width:628px}
.topline{position:absolute;top:0;left:0;width:800px;height:3px;background:#8a8a8a}
.feedback{position:absolute;top:0;left:634px;width:80px;height:24px;background:#8a8a8a;color:#fff;font-size:9px;letter-spacing:.5px;text-align:center;line-height:26px}
.brand{position:absolute;top:26px;left:92px;display:flex;align-items:center;gap:7px;font-size:30px;font-weight:700;color:var(--blue)}
.brand-dot{width:12px;height:12px;border-radius:50%;background:var(--orange)}
.nav{position:absolute;top:48px;right:86px;font-size:9.5px;color:#333;display:flex;gap:8px}
.nav span.sep{color:#555}
.search{top:73px;height:50px;background:linear-gradient(#3596d6,var(--blue-dark));display:flex;align-items:center;padding:0 17px}
.search h2{font-size:17px;font-weight:400;color:#fff;line-height:1.1}
.search p{font-size:8.5px;color:#d9ecf8}
.search-input{margin-left:14px;width:254px;height:27px;background:#fff;font-size:8.5px;color:#777;padding:8px 11px}
.btn-buy,.btn-rent{height:27px;width:57px;color:#fff;font-size:11px;text-align:center;line-height:27px;margin-left:16px}
.btn-buy{background:var(--orange)}
.btn-rent{background:var(--green);margin-left:2px}
.hero{top:126px;height:214px;background:linear-gradient(90deg,#454545,#5a5a5a 50%,#4a4a4a)}
.hero-shadow{position:absolute;top:340px;left:96px;width:608px;height:18px;background:radial-gradient(ellipse at top,rgba(0,0,0,.22),transparent 70%)}
.hero h1{position:absolute;top:28px;left:18px;font-size:19px;font-weight:400;color:var(--orange)}
.hero-copy{position:absolute;top:56px;left:18px;width:226px;font-size:9.2px;line-height:14.6px;color:#fff}
.hero-btn{position:absolute;top:146px;height:24px;background:var(--blue);color:#fff;font-size:9.5px;line-height:24px;padding:0 12px}
.hero-visual{position:absolute;top:21px;left:260px;width:356px;height:162px;border:3px solid #ddd;background:radial-gradient(circle at 52% 50%,#ffffff,#e9f2f9 60%,#dfe8f0)}
.dots{position:absolute;top:196px;left:295px;display:flex;gap:3px}
.dots i{width:6px;height:6px;border-radius:50%;background:#fff}
.dots i:first-child{background:var(--orange)}
.intro{position:absolute;top:370px;left:100px;width:600px;text-align:center}
.intro h2{font-size:20.5px;font-weight:400;color:var(--blue-text)}
.intro p{margin-top:8px;font-size:8.2px;line-height:14.5px;color:#444}
.band-gray{position:absolute;left:0;width:800px;background:var(--gray-bg)}
.card{position:absolute;top:493px;width:200px;height:107px;background:#fff;border:1px solid #e2e2e2;box-shadow:0 4px 6px -3px rgba(0,0,0,.15);padding:10px 12px}
.card h3{display:flex;align-items:center;gap:6px;font-size:13.5px;font-weight:400;color:var(--blue-text);margin-bottom:7px;white-space:nowrap}
.card ul,.cities ul{list-style:none}
.card li{font-size:8.5px;line-height:16px;padding-left:11px;position:relative;color:#444;white-space:nowrap}
.card li::before,.cities li::before{content:"";position:absolute;left:0;top:6px;width:4px;height:4px;border-radius:50%;background:var(--blue)}
.eco{top:642px;height:48px;border:2px solid var(--green);background:linear-gradient(90deg,var(--blue-dark),#3596d6);border-radius:3px;padding:8px 60px 0 12px;font-family:"Noto Serif",Georgia,serif;color:#fff;white-space:nowrap}
.eco-head{display:block;font-size:9px;font-weight:700;letter-spacing:-.3px;line-height:13px}
.eco-line{font-size:8.5px;font-weight:400;letter-spacing:-.2px;line-height:16px}
.eco .eco-btn{display:inline-block;margin-left:6px;background:var(--green);border:1px solid #fff;border-radius:2px;font-family:"Nunito Sans",Arial,sans-serif;font-size:6.5px;line-height:9px;padding:0 10px;vertical-align:middle;letter-spacing:0}
.eco-tree{position:absolute;right:8px;top:4px;width:36px;height:36px}
.tile{position:absolute;top:706px;width:200px;height:125px;background:var(--blue);padding:6px 6px 0}
.tile .photo{height:84px}
.tile .cap{display:flex;justify-content:space-between;align-items:center;height:35px;padding:0 2px;color:#fff;font-size:9.5px}
.tile .cap b{font-size:13px;font-weight:400;color:var(--orange)}
.cities h2{position:absolute;top:866px;left:86px;display:flex;align-items:center;gap:8px;font-size:15px;font-weight:400;color:var(--blue-text)}
.cities ul{position:absolute;top:897px}
.cities li{position:relative;font-size:8.5px;line-height:16px;padding-left:12px;color:#333}
.footer{position:absolute;top:1130px;left:0;width:800px;height:70px;background:var(--footer);color:#bbb;font-size:8.5px}
.footer-links{position:absolute;top:21px;left:86px}
.footer-copy{position:absolute;top:37px;left:86px}
.connect{position:absolute;top:22px;right:86px;display:flex;align-items:center;gap:6px;color:#fff;font-size:8.5px}
.connect i{width:26px;height:26px;border-radius:3px;background:#3b5a9a}
.connect i+i{background:#2aa3e0}
</style>
</head>
<body>
<div class="topline"></div>
<div class="feedback">FEEDBACK</div>
<div class="brand"><span>Pravilo</span><span class="brand-dot"></span></div>
<nav class="nav"><span>Home</span><span class="sep">|</span><span>Advertise Your Properties</span><span class="sep">|</span><span>FAQ</span><span class="sep">|</span><span>Contact Us</span></nav>

<section class="wrap search">
  <div><h2>Search Current Listings</h2><p>Find your next home or rental on PRAVILO today!</p></div>
  <div class="search-input">Enter City State or a Zip</div>
  <div class="btn-buy">BUY</div><div class="btn-rent">RENT</div>
</section>

<section class="wrap hero">
  <h1>Welcome to Pravilo</h1>
  <p class="hero-copy">PRAVILO.com markets your for sale or for rent properties to the most used real estate websites on the internet.<br>Manage one listing and nightly we will update all of the other sites with your changes!</p>
  <div class="hero-btn" style="left:17px">Submit Listings</div>
  <div class="hero-btn" style="left:124px">Submit Rss Feed</div>
  <div class="hero-visual" role="img" aria-label="Your property plus Pravilo spreading to many partner listing websites"></div>
  <div class="dots"><i></i><i></i><i></i><i></i></div>
</section>
<div class="hero-shadow"></div>

<section class="intro">
  <h2>Online Real Estate Marketing Simplified</h2>
  <p>PRAVILO provides the most exposure for real estate listings. We have helped realtors, for sale by owners, for rent by owners, and many others promote their real estate.&nbsp; Listing your home on PRAVILO is easy and effective. Stop wasting your time managing multiple website listings and let PRAVILO do the work for you!</p>
</section>

<div class="band-gray" style="top:470px;height:160px"></div>
<div class="card" style="left:86px">
  <h3><svg width="20" height="18" viewBox="0 0 20 18"><circle cx="10" cy="5" r="4" fill="#8a6a4a"/><path d="M2 18a8 7 0 0116 0z" fill="#3a6ea5"/></svg>By Realtor</h3>
  <ul><li>Submit One Listing or Thousands</li><li>Promote Open Houses</li><li>Stand Out from the Competition</li><li>Self Promotion</li></ul>
</div>
<div class="card" style="left:300px">
  <h3><svg width="20" height="18" viewBox="0 0 20 18"><circle cx="10" cy="5" r="4" fill="#8a6a4a"/><path d="M2 18a8 7 0 0116 0z" fill="#2c4f7c"/></svg>By Owner</h3>
  <ul><li>Low Cost for Maximum Exposure</li><li>Easy to List &amp; Manage Your Property</li><li>Share with Social Networks &amp; Friends</li><li>Printable Flyer</li></ul>
</div>
<div class="card" style="left:513px;width:199px;padding:10px 8px">
  <h3><svg width="22" height="18" viewBox="0 0 24 18"><circle cx="7" cy="5" r="4" fill="#c89a5a"/><circle cx="17" cy="5" r="4" fill="#8a6a4a"/><path d="M0 18a7 7 0 0114 0zM10 18a7 7 0 0114 0z" fill="#e0a030"/></svg>Property Management</h3>
  <ul style="padding-left:4px"><li>RSS Feed Submission</li><li>One Stop Promo Shop</li><li>Expand Your Network</li><li>Simplified Marketing of Properties</li></ul>
</div>

<section class="wrap eco">
  <span class="eco-head">Pravilo.com is dedicated to creating a superior real estate hub and is equally dedicated to preserving our planet.</span>
  <span class="eco-line">For every single paid listing on Pravilo.com we will donate one tree to our conservation partner.</span><span class="eco-btn">Advertise Today</span>
  <div class="eco-tree" role="img" aria-label="Small green tree" style="background:radial-gradient(circle at 50% 40%,#7cc242,#3f8a1f 70%,transparent 72%)"></div>
</section>

<div class="tile" style="left:86px"><div class="photo" role="img" aria-label="Large white house with columns, sold" style="background:linear-gradient(#7fa8d6,#c9d6e2 45%,#6f7f5a)"></div><div class="cap">DearBorn, MI<b>FOR SOLD</b></div></div>
<div class="tile" style="left:300px"><div class="photo" role="img" aria-label="Stone house with gray roof, for sale" style="background:linear-gradient(#8fb3dc,#b8b8b0 50%,#6b7a4e)"></div><div class="cap">Porterville, UT<b>FOR SALE</b></div></div>
<div class="tile" style="left:513px"><div class="photo" role="img" aria-label="Cream villa with swimming pool, for rent" style="background:linear-gradient(#9cc0e4,#e6dcc4 50%,#5aa6c8)"></div><div class="cap">Garland, Texas<b>FOR RENT</b></div></div>

<div class="band-gray" style="top:848px;height:282px"></div>
<section class="cities">
  <h2><svg width="16" height="22" viewBox="0 0 16 22"><path d="M8 0a8 8 0 018 8c0 6-8 14-8 14S0 14 0 8a8 8 0 018-8z" fill="#b5b5b5"/></svg>Popular Cities</h2>
  <ul style="left:86px"><li>ORLANDO, FL</li><li>MESA, AZ</li><li>ORANGE PARK, FL</li><li>SAINT PETERSBURG, FL</li><li>HALLSVILLE, MO</li><li>NORTHAMPTON, PA</li><li>JACKSONVILLE, FL</li><li>Hooper, UT</li><li>Orange Park, Florida</li><li>Valrico, FL</li><li>Plant City, FL</li><li>Delray Beach, FL</li><li>Wesley Chapel, FL</li></ul>
  <ul style="left:219px"><li>Clearwater, Florida</li><li>Altamonte Springs, FL</li><li>Zephyrhills, FL</li><li>Coconut Creek, Fl</li><li>New Port Richey, FL</li><li>Port Richey, FL</li><li>Washington Terrace, UT</li><li>Allen, Texas</li><li>Garland, Texas</li><li>Ruskin, FL</li><li>Apollo Beach, FL</li><li>ASTORIA, NY</li><li>BARTLETT, IL</li></ul>
  <ul style="left:352px"><li>PEORIA, AZ</li><li>MEDFORD, OR</li><li>SHREVEPORT, LA</li><li>LAYTON, UT</li><li>SURPRISE, AZ</li><li>SYRACUSE, UT</li><li>Atlantic Beach, Florida</li><li>Temple Terrace, FL</li><li>Seminole, FL</li><li>Plantation, Florida</li><li>Plantation, Fl</li><li>Pinellas Park, FL</li><li>Kissimmee, FL</li></ul>
  <ul style="left:478px"><li>ROY, UT</li><li>PEORIA, AZ</li><li>MEDFORD, OR</li><li>SHREVEPORT, LA</li><li>LAYTON, UT</li><li>SURPRISE, AZ</li><li>SYRACUSE, UT</li><li>Atlantic Beach, Florida</li><li>Temple Terrace, FL</li><li>Seminole, FL</li><li>Plantation, Florida</li><li>Plantation, Fl</li><li>Pinellas Park, FL</li></ul>
  <ul style="left:607px"><li>ROY, UT</li><li>PEORIA, AZ</li><li>MEDFORD, OR</li><li>SHREVEPORT, LA</li><li>LAYTON, UT</li><li>SURPRISE, AZ</li><li>SYRACUSE, UT</li><li>Atlantic Beach, Florida</li><li>Temple Terrace, FL</li><li>Seminole, FL</li><li>Plantation, Florida</li><li>Plantation, Fl</li><li>Pinellas Park, FL</li></ul>
</section>

<footer class="footer">
  <div class="footer-links">Home &nbsp;|&nbsp; ListBase© RSS Feed Replacement &nbsp;|&nbsp; Submit Your Listings &nbsp;|&nbsp; Contact Pravilo</div>
  <div class="footer-copy">© 2014 Pravilo LLC. All rights reserved.</div>
  <div class="connect">Connect Us:&nbsp;&nbsp;<i></i><i></i></div>
</footer>
</body>
</html>
```